Marketing Flyer

I need a flyer for my marketing company. I would like for it to to be consistent with my logo and business card design. I would also like for there to be an image of a crowded waiting room, or restaurant with people gathered around a flat screen that reads "Your Ad Here".

• logo, info on attached doc.
• Possibly a picture people in a waiting room or restaurant with a digital sign present that reads "your ad here".

```html
<!DOCTYPE html>
<html lang="en">
<head>
<meta charset="utf-8">
<title>Meadowline Marketing – Advertising Flyer</title>
<link href="https://fonts.googleapis.com/css2?family=Montserrat:ital,wght@0,400;0,500;0,700;0,800;1,700&display=swap" rel="stylesheet">
<style>
  :root{
    --green:#7dc242;
    --grey-text:#4d4d4f;
    --grey-logo:#636466;
    --white:#ffffff;
    --photo-dark:#1d2328;
    --photo-mid:#4a5560;
    --photo-light:#aab3b8;
  }
  html,body{margin:0;padding:0;overflow:hidden;}
  body{width:900px;height:1200px;background:var(--white);font-family:"Montserrat",Arial,sans-serif;color:var(--grey-text);}
  .flyer{position:relative;width:900px;height:1200px;overflow:hidden;background:var(--white);}
  .hero{position:absolute;left:0;top:0;width:900px;height:640px;display:block;}
  .content{position:absolute;left:65px;right:65px;top:652px;}
  .headline{margin:0;color:var(--green);font-weight:800;font-size:33.5px;letter-spacing:-.2px;}
  .what-we-do{margin:20px 0 0;font-size:19px;line-height:24px;font-weight:700;color:var(--grey-text);}
  .what-we-do em{font-style:italic;}
  .benefits{display:flex;gap:30px;margin-top:34px;}
  .benefit-list{list-style:none;margin:0;padding:0;flex:1;}
  .benefit-list.right{flex:0 0 372px;}
  .benefit{position:relative;padding-left:25px;font-size:15.5px;line-height:19.5px;letter-spacing:.3px;margin-bottom:10px;}
  .benefit strong{font-weight:700;}
  .tick{position:absolute;left:0;top:3px;width:14px;height:14px;}
  .brand{position:absolute;left:0;right:0;top:1078px;text-align:center;}
  .brand-name{display:block;font-size:72px;font-weight:700;color:var(--grey-logo);letter-spacing:-1.5px;line-height:78px;}
  .brand-sub{display:block;font-size:22px;font-weight:400;letter-spacing:13px;color:var(--grey-logo);margin-top:-4px;padding-left:13px;}
</style>
</head>
<body>
<div class="flyer">
  <svg class="hero" viewBox="0 0 900 640" xmlns="http://www.w3.org/2000/svg">
    <defs>
      <linearGradient id="photoTone" x1="0" y1="0" x2="0" y2="1">
        <stop offset="0" stop-color="var(--photo-dark)"/>
        <stop offset=".35" stop-color="var(--photo-mid)"/>
        <stop offset=".55" stop-color="var(--photo-light)"/>
        <stop offset="1" stop-color="var(--photo-dark)"/>
      </linearGradient>
    </defs>
    <rect role="img" aria-label="Photo of a crowded trade show hall with green hanging signs reading Your Ad Here" x="0" y="0" width="900" height="640" fill="url(#photoTone)"/>
    <path class="swoosh" fill="var(--green)" d="M0,378 C25,440 80,470 190,492 C400,528 620,552 780,600 L900,640 L900,612 C760,606 640,560 470,556 C300,552 150,530 0,470 Z"/>
    <path class="swoosh-branch" fill="var(--green)" d="M380,556 C420,566 470,575 500,590 C460,586 420,578 380,568 Z"/>
    <path class="page-edge" fill="var(--white)" d="M0,480 C140,540 290,560 420,565 C590,570 700,622 900,622 L900,640 L0,640 Z"/>
    <path fill="var(--white)" d="M0,470 C150,530 300,552 470,556 C640,560 760,606 900,612 L900,640 L0,640 Z" opacity="0"/>
  </svg>

  <main class="content">
    <h1 class="headline">Benefits of Advertising with Meadowline</h1>
    <p class="what-we-do">What we do: <em>We design an ad for your company and place it on the TV at local businesses.</em></p>

    <div class="benefits">
      <ul class="benefit-list left">
        <li class="benefit"><svg class="tick" viewBox="0 0 14 14"><circle cx="7" cy="7" r="5.5" fill="none" stroke="var(--grey-text)" stroke-width="1.3"/><path d="M4.5,7 L6.7,9.2 L12.5,2.5" fill="none" stroke="var(--grey-text)" stroke-width="1.5"/></svg><strong>Inexpensive:</strong> Only $31.00 per month!</li>
        <li class="benefit"><svg class="tick" viewBox="0 0 14 14"><circle cx="7" cy="7" r="5.5" fill="none" stroke="var(--grey-text)" stroke-width="1.3"/><path d="M4.5,7 L6.7,9.2 L12.5,2.5" fill="none" stroke="var(--grey-text)" stroke-width="1.5"/></svg><strong>Exposure:</strong> Our digital signage is placed in only the best/high traffic businesses in your area.</li>
        <li class="benefit"><svg class="tick" viewBox="0 0 14 14"><circle cx="7" cy="7" r="5.5" fill="none" stroke="var(--grey-text)" stroke-width="1.3"/><path d="M4.5,7 L6.7,9.2 L12.5,2.5" fill="none" stroke="var(--grey-text)" stroke-width="1.5"/></svg><strong>Repetition:</strong> Your ad is shown over 3,500 time each month (42,000 times per year)!</li>
        <li class="benefit"><svg class="tick" viewBox="0 0 14 14"><circle cx="7" cy="7" r="5.5" fill="none" stroke="var(--grey-text)" stroke-width="1.3"/><path d="M4.5,7 L6.7,9.2 L12.5,2.5" fill="none" stroke="var(--grey-text)" stroke-width="1.5"/></svg><strong>Local:</strong> We show your ad to consumers in YOUR area. Let us help you do business with the people you want to do business with.</li>
      </ul>
      <ul class="benefit-list right">
        <li class="benefit"><svg class="tick" viewBox="0 0 14 14"><circle cx="7" cy="7" r="5.5" fill="none" stroke="var(--grey-text)" stroke-width="1.3"/><path d="M4.5,7 L6.7,9.2 L12.5,2.5" fill="none" stroke="var(--grey-text)" stroke-width="1.5"/></svg><strong>Exclusivity:</strong> Only 2 ads per industry.</li>
        <li class="benefit"><svg class="tick" viewBox="0 0 14 14"><circle cx="7" cy="7" r="5.5" fill="none" stroke="var(--grey-text)" stroke-width="1.3"/><path d="M4.5,7 L6.7,9.2 L12.5,2.5" fill="none" stroke="var(--grey-text)" stroke-width="1.5"/></svg><strong>Lead Generation:</strong> We show consumers how to reach you and where to find you.</li>
        <li class="benefit"><svg class="tick" viewBox="0 0 14 14"><circle cx="7" cy="7" r="5.5" fill="none" stroke="var(--grey-text)" stroke-width="1.3"/><path d="M4.5,7 L6.7,9.2 L12.5,2.5" fill="none" stroke="var(--grey-text)" stroke-width="1.5"/></svg><strong>Brand Awareness:</strong> People need to know your business. We make that happen by putting your brand right in front of them.</li>
        <li class="benefit"><svg class="tick" viewBox="0 0 14 14"><circle cx="7" cy="7" r="5.5" fill="none" stroke="var(--grey-text)" stroke-width="1.3"/><path d="M4.5,7 L6.7,9.2 L12.5,2.5" fill="none" stroke="var(--grey-text)" stroke-width="1.5"/></svg><strong>Digital:</strong> Digital advertising has higher retention rates and higher consumer engagement.</li>
      </ul>
    </div>
  </main>

  <footer class="brand">
    <span class="brand-name">Meadowline</span>
    <span class="brand-sub">MARKETING</span>
  </footer>
</div>
</body>
</html>
```